Open House 2017

We need a flyer for an insert for a newspaper for an open house that we are going to have and we are also wanting to list the front of the flyer the 3 pictures of our real estate agents and our Logo.

For the real estate agents : The one with Purple shirt would be the middle picture.

Attached also is our current Logo, Please re-design our Logo a bit to make it look better.

Target Market(s)

Residential and commercial and Land In our rural areas.

Industry/Entity Type

House

Requirements
Must have
• Front page -
• Our logo at the top our 3 pictures at the top after our logo and business address.
• Middle of page Some thing worded similar to the following:"let us place a SOLD sign in your front yard". Or
• " Sold vs. For Sale which would you like to see in your front yard?"
• Our colors for our agency are Gold and Black (the whole flyer does not need to be this color though)
• Join us for an open house in our office
• Wednesday March 1
• 3-6pm
• Back page of flyer: "If you would like to add your name to the Sold Properties list, give us a call today!
• Sold listings which we will get sent to you will also be listed on the back page.
Should not have
• do not make the flyer too "busy" with too many pictures and wording.

```html
<!DOCTYPE html>
<html lang="en">
<head>
<meta charset="utf-8">
<title>Carvell Realty LLC – Open House</title>
<link rel="stylesheet" href="https://fonts.googleapis.com/css2?family=Cinzel:wght@700;800&family=Libre+Baskerville:ital,wght@0,400;1,700&display=swap">
<style>
  :root {
    --black: #050505;
    --gold: #e2a31f;
    --gold-deep: #c98d18;
    --gold-light: #f8dc9a;
    --gold-pale: #fbe7b3;
    --ink: #0d0a05;
    --cream: #fff3cf;
  }
  * { margin: 0; padding: 0; box-sizing: border-box; }
  html, body { width: 934px; height: 1200px; overflow: hidden; background: var(--black); }
  .flyer { position: relative; width: 934px; height: 1200px; overflow: hidden; font-family: "Cinzel", "Times New Roman", serif; }

  .masthead { position: absolute; top: 0; left: 0; width: 934px; height: 176px; background: var(--black); border-bottom: 2px solid var(--gold-light); text-align: center; }
  .brand-name { position: absolute; top: 40px; left: 0; width: 100%; font-family: "Cinzel", serif; font-weight: 800; font-size: 64px; line-height: 1; color: var(--gold); letter-spacing: 1px; }
  .tagline { position: absolute; top: 128px; left: 0; width: 100%; font-family: "Libre Baskerville", Georgia, serif; font-weight: 400; font-size: 22px; letter-spacing: 1px; color: var(--gold-light); }

  .stage { position: absolute; top: 178px; left: 0; width: 934px; height: 906px;
    background: radial-gradient(ellipse at 60% 45%, var(--gold-pale) 0%, var(--gold-light) 35%, #eebc55 75%, var(--gold-deep) 100%); }
  .swoosh { position: absolute; inset: 0; width: 100%; height: 100%; }

  .agents { position: absolute; top: 72px; left: 0; width: 100%; height: 250px; }
  .agent { position: absolute; width: 236px; height: 236px; border-radius: 50%; }
  .agent::before { content: ""; position: absolute; inset: -2px -10px -10px -2px; border-radius: 50%; background: var(--gold-deep); z-index: 0; }
  .agent-photo { position: absolute; inset: 0; border-radius: 50%; border: 2px solid var(--gold); z-index: 1;
    background: radial-gradient(circle at 50% 40%, #a9a6a2 0%, #7f7d7b 60%, #6b6a69 100%); }
  .agent-1 { left: 80px; }
  .agent-2 { left: 336px; }
  .agent-3 { left: 608px; }

  .copy { position: absolute; left: 0; width: 100%; text-align: center; color: var(--ink); font-weight: 700; white-space: nowrap;
    text-shadow: 1px 1px 0 var(--cream), -1px -1px 0 var(--cream), 1px -1px 0 var(--cream), -1px 1px 0 var(--cream), 2px 3px 3px rgba(90,55,0,.35); }
  .headline { top: 360px; font-size: 44px; line-height: 62px; letter-spacing: 1px; }
  .invite-lead { top: 528px; font-size: 34px; line-height: 40px; }
  .invite-title { top: 568px; font-size: 66px; line-height: 76px; letter-spacing: 1px; }
  .event-details { top: 668px; font-size: 44px; line-height: 66px; }

  .footer { position: absolute; top: 1084px; left: 0; width: 934px; height: 116px; background: var(--black); text-align: center; }
  .copyright { padding-top: 34px; font-family: "Libre Baskerville", Georgia, serif; font-style: italic; font-weight: 700; font-size: 26px; color: var(--gold); }
</style>
</head>
<body>
<div class="flyer">
  <header class="masthead">
    <div class="brand-name">Carvell Realty LLC</div>
    <div class="tagline">Your neighbors in every move.</div>
  </header>

  <main class="stage">
    <svg class="swoosh" viewBox="0 0 934 906" preserveAspectRatio="none" aria-hidden="true">
      <path d="M0 0 H215 C190 180 230 420 360 600 C440 710 520 800 580 906 H0 Z" fill="#d9a238" opacity=".35"/>
      <path d="M0 650 C120 700 300 760 420 906 H0 Z" fill="#c98d18" opacity=".35"/>
      <path d="M0 690 C140 740 280 800 360 906" stroke="#f7d88f" stroke-width="3" fill="none" opacity=".6"/>
    </svg>

    <section class="agents">
      <div class="agent agent-1"><div class="agent-photo" role="img" aria-label="Portrait of agent in white blouse"></div></div>
      <div class="agent agent-2"><div class="agent-photo" role="img" aria-label="Portrait of agent in purple shirt"></div></div>
      <div class="agent agent-3"><div class="agent-photo" role="img" aria-label="Portrait of agent in checked shirt"></div></div>
    </section>

    <h1 class="copy headline">LET US PLACE A "SOLD" SIGN<br>IN YOUR FRONT YARD</h1>
    <p class="copy invite-lead">JOIN US FOR AN</p>
    <h2 class="copy invite-title">OPEN HOUSE</h2>
    <p class="copy event-details">WEDNEDAY MARCH 1<br>FROM 3-6PM<br>48 N. HARBOR STREET</p>
  </main>

  <footer class="footer">
    <p class="copyright">© Copyright 2017 Carvell Realty LLC</p>
  </footer>
</div>
</body>
</html>
```